Quorvane Capital Modern Business Card

We need a modern business card template designed for Quorvane Capital.
Quorvane Capital is a diversified global cryptocurrency investment fund.

The font under the logo: Hiragino Kaku Gothic Pro

Color Hexcode: Main colors white (ffffff) & teal (188383), we are open to adding #fcca46 as an accent

Target Market(s)

Accredited Investors, high net worth individuals and institutional investors

Industry/Entity Type

Investment

Contact Information for Business Card

Contact Information should contain
Name
main phone +1 720 555 0147
cell
email

Font styles to use
Sans Serif
Other font styles liked:
• Hiragino Kaku Gothic Pro

Requirements
Must have
• would like to have icons that identify the contact information
• include our website: www.quorvanecapital.example
• include our Tagline: Diversified Crypto Investment Funds
Nice to have
• Would like to have a simple back side with the logo (without the words) and plenty of space

```html
<!DOCTYPE html>
<html lang="en">
<head>
<meta charset="utf-8">
<title>Quorvane Capital Business Card</title>
<link href="https://fonts.googleapis.com/css2?family=Jost:wght@400;500&display=swap" rel="stylesheet">
<style>
  :root {
    --teal: #1b9393;
    --white: #ffffff;
    --backdrop: #eef0ef;
    --tagline: #9fd0cf;
    --website: #b6dcdb;
  }
  * { margin: 0; padding: 0; box-sizing: border-box; }
  html, body {
    width: 1200px;
    height: 1200px;
    overflow: hidden;
    background: var(--backdrop);
    font-family: "Jost", sans-serif;
  }
  .canvas {
    position: relative;
    width: 1200px;
    height: 1200px;
  }
  .card {
    position: absolute;
    top: 276px;
    width: 359px;
    height: 629px;
    border-radius: 12px;
    overflow: hidden;
  }
  .card-front {
    left: 197px;
    background: var(--teal);
    color: var(--white);
    text-align: center;
  }
  .card-back {
    left: 633px;
    background: var(--white);
    color: var(--teal);
  }
  .brand-name {
    position: absolute;
    top: 379px;
    left: 0;
    right: 0;
    font-size: 23px;
    font-weight: 400;
    letter-spacing: 0.5px;
  }
  .tagline {
    position: absolute;
    top: 528px;
    left: 0;
    right: 0;
    font-size: 14px;
    line-height: 19px;
    color: var(--tagline);
    letter-spacing: 0.3px;
  }
  .website {
    position: absolute;
    top: 573px;
    left: 0;
    right: 0;
    font-size: 17px;
    color: var(--website);
    letter-spacing: 0.3px;
  }
  .holder {
    position: absolute;
    top: 42px;
    left: 42px;
  }
  .holder-name {
    font-size: 20px;
    font-weight: 400;
    line-height: 22px;
  }
  .holder-title {
    font-size: 15px;
    line-height: 19px;
  }
  .contact {
    position: absolute;
    top: 462px;
    left: 36px;
    right: 20px;
    list-style: none;
    font-size: 18px;
    line-height: 25px;
  }
  .contact-item {
    display: flex;
    align-items: center;
    gap: 10px;
    white-space: nowrap;
  }
  .contact-icon {
    flex: 0 0 16px;
    width: 16px;
    height: 16px;
    fill: none;
    stroke: var(--teal);
    stroke-width: 1.8;
    stroke-linecap: round;
    stroke-linejoin: round;
  }
  .contact-icon.no-icon { stroke: none; }
</style>
</head>
<body>
<main class="canvas">
  <section class="card card-front" aria-label="Card front">
    <div class="brand-name">QUORVANE CAPITAL</div>
    <div class="tagline">DIVERSIFIED CRYPTO<br>INVESTMENT FUNDS</div>
    <div class="website">www.quorvanecapital.example</div>
  </section>
  <section class="card card-back" aria-label="Card back">
    <div class="holder">
      <div class="holder-name">DANA WHITFIELD</div>
      <div class="holder-title">Chief Executive Officer</div>
    </div>
    <ul class="contact">
      <li class="contact-item">
        <svg class="contact-icon" viewBox="0 0 16 16" aria-hidden="true"><path d="M8 15s5-5 5-8.5A5 5 0 0 0 3 6.5C3 10 8 15 8 15z"/><circle cx="8" cy="6.5" r="1.8"/></svg>
        <span>418 Larkspur Lane</span>
      </li>
      <li class="contact-item">
        <svg class="contact-icon no-icon" viewBox="0 0 16 16" aria-hidden="true"></svg>
        <span>Los Angeles, CA</span>
      </li>
      <li class="contact-item">
        <svg class="contact-icon" viewBox="0 0 16 16" aria-hidden="true"><path d="M3 1.8h3l1.3 3.4-1.8 1.2a8 8 0 0 0 4.1 4.1l1.2-1.8 3.4 1.3v3a1.3 1.3 0 0 1-1.4 1.3A12.5 12.5 0 0 1 1.7 3.2 1.3 1.3 0 0 1 3 1.8z"/></svg>
        <span>+1 720 555 0147</span>
      </li>
      <li class="contact-item">
        <svg class="contact-icon" viewBox="0 0 16 16" aria-hidden="true"><rect x="4" y="1.5" width="8" height="13" rx="1.5"/><path d="M7 12.2h2"/></svg>
        <span>843-555-0193</span>
      </li>
      <li class="contact-item">
        <svg class="contact-icon" viewBox="0 0 16 16" aria-hidden="true"><rect x="1.5" y="3.5" width="13" height="9" rx="1"/><path d="M2 4l6 5 6-5"/></svg>
        <span>dana@quorvanecapital.example</span>
      </li>
    </ul>
  </section>
</main>
</body>
</html>
```